Tax & Accounting business needs business card design

Looking for a professional classy business card for a tax and accounting business. We offer quality, professional services to individuals and small businesses including tax preparation and planning, accounting and bookkeeping, payroll services, and business consulting.

I am an Enrolled Agent (EA) which is a Federally Licensed Tax Practitioner. I am licensed to represent taxpayers before the ZTQ.

We want to stand out from all the other "boring" tax & accounting firms without being over the top.

We have a well established firm in one location and are now opening a second location.

• Logo
• Logo color scheme
• Both location addresses
• Front and back of card
• Please see my sample business card (attached) for location addresses, phone numbers, ect. Although you may get some inspiration from this sample card, this is my own unqualified and bad attempt at designing my own card which I'm not happy with.

```html
<!DOCTYPE html>
<html lang="en">
<head>
<meta charset="utf-8">
<title>Ledgerline Books LLC — Business Card</title>
<link rel="stylesheet" href="https://fonts.googleapis.com/css2?family=Cinzel:wght@500&family=Open+Sans:wght@400;600;700&display=swap">
<style>
  :root {
    --navy-deep: #05072a;
    --navy: #0d1155;
    --royal: #2b3fe0;
    --teal: #1f6b62;
    --slate: #6e6e78;
    --white: #ffffff;
    --paper: #e9e6e1;
  }
  * { margin: 0; padding: 0; box-sizing: border-box; }
  html, body { width: 1200px; height: 723px; overflow: hidden; }
  body {
    background: var(--paper);
    font-family: "Open Sans", Arial, sans-serif;
    position: relative;
  }
  .card {
    position: absolute;
    top: 207px;
    width: 540px;
    height: 309px;
    overflow: hidden;
    border-radius: 3px;
    background: radial-gradient(ellipse at 45% 40%, var(--navy) 0%, var(--navy-deep) 85%);
    box-shadow: 0 6px 18px rgba(0,0,0,0.25);
    color: var(--white);
  }
  .card--front { left: 40px; }
  .card--back { left: 620px; }

  /* Front */
  .header-band {
    position: absolute; left: 0; top: 0; width: 540px; height: 96px;
    background: var(--white);
    border-bottom: 4px solid var(--royal);
  }
  .brand-front {
    position: absolute; left: 0; top: 30px; width: 540px; text-align: center;
    font-family: "Open Sans", Arial, sans-serif; font-weight: 600;
    color: var(--teal); font-size: 26px; line-height: 1.2;
  }
  .holder {
    position: absolute; left: 28px; top: 108px;
    font-weight: 700; font-size: 21px; line-height: 1.3; letter-spacing: 0.3px;
  }
  .holder-rule {
    position: absolute; left: 28px; top: 140px; width: 300px; height: 2px;
    background: var(--slate);
  }
  .email { position: absolute; left: 28px; top: 146px; font-size: 13px; font-weight: 600; line-height: 1.3; }
  .office {
    position: absolute; top: 172px; font-size: 9.5px; line-height: 12px;
  }
  .office--santa-fe { left: 28px; }
  .office--albuquerque { left: 290px; }
  .office-title { font-weight: 600; }
  .rule { position: absolute; left: 0; width: 540px; height: 2px; background: var(--white); }
  .rule--top { top: 238px; }
  .rule--bottom { top: 270px; }
  .website {
    position: absolute; left: 28px; top: 241px;
    font-size: 20px; line-height: 27px; font-weight: 700; letter-spacing: 0.4px;
  }
  .credential {
    position: absolute; left: 12px; top: 276px;
    font-size: 10px; font-weight: 600; line-height: 13px;
  }

  /* Back */
  .brand-back {
    position: absolute; left: 40px; top: 80px; width: 460px;
    font-family: "Open Sans", Arial, sans-serif; font-weight: 600;
    color: var(--teal); font-size: 36px; line-height: 1.2; text-align: center;
  }
  .tagline {
    position: absolute; left: 0; width: 540px; top: 208px; text-align: center;
    font-family: "Cinzel", Georgia, serif; font-size: 16px; line-height: 22px; letter-spacing: 2.5px;
  }
  .back-rule {
    position: absolute; left: 40px; top: 238px; width: 460px; height: 2px;
    background: var(--white);
  }
  .services {
    position: absolute; left: 0; width: 540px; top: 248px; text-align: center;
    font-family: "Cinzel", Georgia, serif; font-size: 14px; line-height: 20px; letter-spacing: 2px;
  }
  .services .dot {
    display: inline-block; width: 6px; height: 6px; background: var(--white);
    margin: 0 8px; vertical-align: middle;
  }
</style>
</head>
<body>

<section class="card card--front" aria-label="Card front">
  <div class="header-band"></div>
  <div class="brand-front">Ledgerline Books LLC</div>

  <div class="holder">Marisol T. Vega, EA</div>
  <div class="holder-rule"></div>
  <div class="email">marisol@ledgerlinebooks.com</div>

  <div class="office office--santa-fe">
    <div class="office-title">Santa Fe Office</div>
    <div>840 W Alameda Ave Ste B</div>
    <div>Santa Fe, NM 87501</div>
    <div>ofc 505.555.0146</div>
    <div>fax 505.555.0147</div>
  </div>
  <div class="office office--albuquerque">
    <div class="office-title">Albuquerque Office</div>
    <div>3320 Menaul Blvd NE Ste 4</div>
    <div>Albuquerque, NM 87107</div>
    <div>ofc 505.555.0188</div>
    <div>fax 505.555.0177</div>
  </div>

  <div class="rule rule--top"></div>
  <div class="website">www.ledgerline-nm.com</div>
  <div class="rule rule--bottom"></div>
  <div class="credential">
    Enrolled agent - Federally licensed tax practitioner<br>
    Licensed to represent taxpayers before the ZTQ
  </div>
</section>

<section class="card card--back" aria-label="Card back">
  <div class="brand-back">Ledgerline<br>Books LLC</div>
  <div class="tagline">PROFESSIONAL BUSINESS SERVICES</div>
  <div class="back-rule"></div>
  <div class="services">TAXES<span class="dot"></span>ACCOUNTING<span class="dot"></span>BOOKKEEPING<span class="dot"></span>PAYROLL</div>
</section>

</body>
</html>
```